Fence Contractor Website Design

We are working with Yardline Works. They are a local fencing and automatic gate installer and in need of a new website design.
Some sites to use for inspiration:
https://pinevalebarrier.example
https://marwickrails.example
https://www.tellurpostsandboards.example
https://www.grovanpaneling.example
Thank you for taking the time to consider designing a website for us. We are web developers based in Stockton, CA, USA. Most of our projects go through the same process. Understanding this process may help you win a project with us. We custom-code all of our websites in-house. We don’t have any requirements as to what tools you use for your design, but we prefer Figma files. For any design that we label as four-stars, we send it to the client for review. The client picks the final design they want us to use. Once we complete this process, we will continue to show additional clients all the four-star sites and purchase them later. Your designs will have multiple chances to sell. For better chances of success, we ask that you follow these guidelines.
IMAGES:
If you use any images or icons in the design, we ask that you have a link to the asset so we can purchase the image/icon. Most of the designs we submit do not have the customer’s images on them unless they have some great images. Be creative; show us the feeling you are trying to portray with your image choices. Use any royalty-free site you choose. We subscribe to Stockvane and mainly use their images, but we can purchase images outside of Stockvane.
PLEASE NOTE: we will not submit designs to clients with watermarks on the images.
FONTS:
We ask that you identify the fonts used in the design. This can be done in a message if you want. We typically use Google Fonts and Stockvane Fonts.
CONTENT:
We're always open to different content and ideas. We often submit designs with stock images so the client can see our vision. We typically take pictures after the website launch to use their images with our vision. Lorem Ipsum is fine for paragraphs, but we ask that you write the headers in correct English. We want to be able to show the vision and identify the sections of the website.
INSPIRATION:
We typically add a couple of links in the brief of websites we like to help you get started in your design.
REVISIONS:
We do not often ask for revisions of the designs unless we see something in the design that may not appeal to the client. If there are slight changes that we want to make, we do that in the development process.
FEEDBACK:
We rarely give feedback on designs during the design process. We are working on many website projects and do not have the time to provide feedback. We usually respond if your request is well thought out and asks specific questions, but a note asking “feedback, please” usually goes unanswered.
Number of Pages Required
1 page
Look and feel
Each slider illustrates characteristics of the customer's brand and the style your logo design should communicate.

```html
<!DOCTYPE html>
<html lang="en">
<head>
<meta charset="utf-8">
<title>Yardline Works — Professional Fencing &amp; Automatic Gates</title>
<link rel="stylesheet" href="https://fonts.googleapis.com/css2?family=Archivo:wght@700;800&family=Inter:wght@400;500;600;700&display=swap">
<style>
:root{
  --navy:#1b2747;
  --mist:#c5c9d3;
  --red:#e0262e;
  --ink:#1f2433;
  --body:#3b4050;
  --muted:#8b90a0;
  --white:#ffffff;
}
*{margin:0;padding:0;box-sizing:border-box}
html,body{width:1200px;height:4896px;overflow:hidden}
body{background:var(--white);font-family:"Inter",sans-serif;color:var(--body);position:relative}
.abs{position:absolute}
.heading{font-family:"Archivo",sans-serif;font-weight:800;text-transform:uppercase;letter-spacing:2px;color:var(--navy);line-height:1.2}
.para{font-size:14px;line-height:21px;color:var(--body)}
.btn{display:flex;align-items:center;justify-content:center;background:var(--white);color:var(--red);font-family:"Inter",sans-serif;font-weight:700;font-size:11px;letter-spacing:1.5px;text-transform:uppercase;text-decoration:none;border-radius:3px}
.photo{border-radius:4px}

/* nav */
.site-nav{top:0;left:0;width:1200px;height:76px;background:var(--white)}
.nav-link{top:31px;font-size:11px;font-weight:600;letter-spacing:1.4px;color:var(--muted);text-transform:uppercase;text-decoration:none}
.nav-link.active{color:var(--ink)}
.nav-link.active::after{content:"";position:absolute;left:0;right:0;top:20px;height:3px;background:var(--red)}
.brand{top:28px;left:520px;width:160px;text-align:center;font-weight:700;font-size:17px;color:var(--navy)}

/* hero */
.hero{top:76px;left:0;width:1200px;height:656px;background:var(--navy)}
.hero-title{top:146px;left:0;width:1200px;text-align:center;color:var(--white);font-size:44px;letter-spacing:3px;line-height:54px}
.hero-btn{top:288px;left:516px;width:168px;height:34px}
.hero-photo{top:452px;left:211px;width:778px;height:409px;background:linear-gradient(180deg,#3f5a34 0%,#8aa07a 45%,#4f7a36 75%,#b9b7b0 100%)}

/* about */
.about-title{top:936px;left:116px;font-size:32px}
.about-text{top:932px;left:700px;width:384px}
.about-text p+p{margin-top:12px}
.about-graphic{top:1036px;left:118px;width:483px;height:209px;background:var(--navy)}
.band{top:1245px;left:0;width:1200px;height:29px;background:var(--navy)}

/* section titles */
.section-title{left:0;width:1200px;text-align:center;font-size:32px;letter-spacing:2.4px;line-height:40px}
.divider{left:563px;width:74px;height:22px;background:var(--navy);border-radius:2px}

/* services */
.service{width:300px}
.service .photo{width:300px;height:233px}
.service h3{margin-top:25px;font-size:15px;font-weight:700;color:var(--ink)}
.service p{margin-top:9px;font-size:11.5px;line-height:20px;color:var(--body)}

/* why */
.why{top:2322px;left:0;width:1200px;height:541px;background:var(--mist)}
.why-title{top:88px;left:116px;font-size:32px}
.why-text{top:196px;left:116px;width:384px;font-size:13.5px}
.why-text p+p{margin-top:18px}
.why-photo{top:42px;left:616px;width:465px;height:416px;background:linear-gradient(180deg,#3a5230 0%,#9aab8c 45%,#4d7735 75%,#bcbab3 100%)}

/* cta */
.cta{left:0;width:1200px;height:298px;background:var(--navy)}
.cta-title{top:84px;left:116px;color:var(--white);font-size:32px;letter-spacing:2.4px}
.cta-text{top:84px;left:616px;width:460px;color:var(--white);font-size:14px;line-height:21px}
.cta-btn{top:177px;left:616px;width:167px;height:34px}

/* gallery */
.tile{border-radius:3px}

/* testimonials */
.reviews{top:3984px;left:0;width:1200px;height:392px;background:var(--mist)}
.reviews-title{top:86px;left:116px;font-size:32px}
.arrow{top:86px;width:34px;height:34px}
.quote{top:188px;width:450px;font-size:13.5px;line-height:21px;color:var(--ink)}
.quote cite{display:block;margin-top:22px;font-style:normal;font-weight:700;font-size:13.5px}

/* footer */
.footer-brand{top:4752px;left:116px;font-weight:700;font-size:17px;color:var(--navy)}
.foot-link{top:4758px;font-size:11px;font-weight:600;letter-spacing:1.4px;color:var(--muted);text-transform:uppercase;text-decoration:none}
.foot-link.active{color:var(--ink)}
.copyright{top:4848px;left:116px;font-size:12px;color:var(--muted)}
.social{top:4840px;width:28px;height:28px;border-radius:50%;background:var(--muted)}
</style>
</head>
<body>

<header class="site-nav abs">
  <a class="nav-link abs active" style="left:214px" href="#">Home</a>
  <a class="nav-link abs" style="left:281px" href="#">About us</a>
  <a class="nav-link abs" style="left:376px" href="#">Our services</a>
  <div class="brand abs">Yardline Works</div>
  <a class="nav-link abs" style="left:724px" href="#">Portfolio</a>
  <a class="nav-link abs" style="left:826px" href="#">FAQ</a>
  <a class="nav-link abs" style="left:880px" href="#">Contact us</a>
</header>

<section class="hero abs">
  <h1 class="heading hero-title abs">Professional fencing<br>&amp; automatic gates</h1>
  <a class="btn hero-btn abs" href="#">Get a free quote</a>
</section>
<div class="photo hero-photo abs" role="img" aria-label="White ornamental metal fence above a trimmed green hedge beside a paved path"></div>

<h2 class="heading about-title abs">The right choice for<br>quality fencing</h2>
<div class="about-text para abs">
  <p>Lorem ipsum dolor sit amet, consectetur adipiscing elit, sed do eiusmod tempor incididunt ut labore et dolore magna aliqua. Ut enim ad minim veniam, quis nostrud exercitation ullamco laboris nisi ut aliquip ex ea commodo consequat.</p>
  <p>Duis aute irure dolor in reprehenderit in voluptate velit esse cillum dolore eu fugiat nulla pariatur. Excepteur sint occaecat cupidatat non proident, sunt in culpa qui officia deserunt mollit anim id est laborum.</p>
</div>
<div class="about-graphic abs" role="img" aria-label="Decorative navy fence illustration"></div>
<div class="band abs"></div>

<h2 class="heading section-title abs" style="top:1358px">Services tailored to<br>your needs</h2>
<div class="divider abs" style="top:1446px" role="img" aria-label="Small decorative heading ornament"></div>

<article class="service abs" style="top:1517px;left:116px"><div class="photo" role="img" aria-label="Blue house behind a white picket fence" style="background:linear-gradient(180deg,#9fc0dc 0%,#4f6f8e 55%,#e9ecef 100%)"></div><h3>Residential fencing</h3><p>Duis aute irure dolor in reprehenderit in voluptate velit esse cillum dolore eu fugiat nulla pariatur sint occaecat.</p></article>
<article class="service abs" style="top:1517px;left:449px"><div class="photo" role="img" aria-label="White ornamental commercial fence with gate posts" style="background:linear-gradient(180deg,#3d5531 0%,#a3b397 55%,#4b7333 100%)"></div><h3>Commercial fencing</h3><p>Duis aute irure dolor in reprehenderit in voluptate velit esse cillum dolore eu fugiat nulla pariatur sint occaecat.</p></article>
<article class="service abs" style="top:1517px;left:781px"><div class="photo" role="img" aria-label="Indoor pool with dark metal pool fence" style="background:linear-gradient(180deg,#eeeeee 0%,#cfd2d3 50%,#2e6f70 100%)"></div><h3>Pool Fences</h3><p>Duis aute irure dolor in reprehenderit in voluptate velit esse cillum dolore eu fugiat nulla pariatur sint occaecat.</p></article>
<article class="service abs" style="top:1893px;left:116px"><div class="photo" role="img" aria-label="Close-up of chain link fence mesh" style="background:linear-gradient(135deg,#3f5a6e 0%,#a8b6bd 50%,#6f8f4d 100%)"></div><h3>Chain link fencing</h3><p>Duis aute irure dolor in reprehenderit in voluptate velit esse cillum dolore eu fugiat nulla pariatur sint occaecat.</p></article>
<article class="service abs" style="top:1893px;left:449px"><div class="photo" role="img" aria-label="Wooden fence around a backyard lawn" style="background:linear-gradient(180deg,#6c7f55 0%,#b7895d 50%,#4f7c2f 100%)"></div><h3>Wood fencing</h3><p>Duis aute irure dolor in reprehenderit in voluptate velit esse cillum dolore eu fugiat nulla pariatur sint occaecat.</p></article>
<article class="service abs" style="top:1893px;left:781px"><div class="photo" role="img" aria-label="Black wrought iron fence with spear tips" style="background:linear-gradient(135deg,#7a5f5c 0%,#5e7b45 50%,#2a2d35 100%)"></div><h3>Iron Fencing</h3><p>Duis aute irure dolor in reprehenderit in voluptate velit esse cillum dolore eu fugiat nulla pariatur sint occaecat.</p></article>

<section class="why abs">
  <h2 class="heading why-title abs">Why choose<br>Yardline Works?</h2>
  <div class="why-text para abs">
    <p>Sed ut perspiciatis unde omnis iste natus error sit voluptatem accusantium doloremque laudantium, totam rem aperiam, eaque ipsa quae ab illo inventore veritatis et quasi architecto beatae vitae dicta sunt explicabo. Nemo enim ipsam voluptatem quia voluptas sit aspernatur aut odit aut fugit.</p>
    <p>Neque porro quisquam est, qui dolorem ipsum quia dolor sit amet, consectetur, adipisci velit, sed quia non numquam eius modi tempora incidunt ut labore et dolore magnam aliquam quaerat voluptatem.</p>
  </div>
  <div class="photo why-photo abs" role="img" aria-label="White ornamental metal fence along a hedge and walkway"></div>
</section>

<section class="cta abs" style="top:2863px">
  <h2 class="heading cta-title abs">Ready to transform<br>your property?</h2>
  <p class="cta-text abs">Lorem ipsum dolor sit amet, consectetur adipiscing elit, sed do eiusmod tempor incididunt ut labore et dolore magna aliqua. Ut enim ad minim veniam, quis nostrud exercitation.</p>
  <a class="btn cta-btn abs" href="#">Get a free quote</a>
</section>

<h2 class="heading section-title abs" style="top:3244px">Browse our fence &amp;<br>gate projects</h2>
<div class="divider abs" style="top:3334px" role="img" aria-label="Small decorative heading ornament"></div>

<div class="tile abs" style="top:3405px;left:17px;width:452px;height:237px;background:linear-gradient(180deg,#7e9a66 0%,#b3aba0 55%,#5f8a36 100%)" role="img" aria-label="Grey wooden fence with flower planter beside a house"></div>
<div class="tile abs" style="top:3405px;left:486px;width:227px;height:237px;background:linear-gradient(180deg,#f0f0f0 0%,#cfd3d4 55%,#2f6e70 100%)" role="img" aria-label="Indoor pool with metal railing"></div>
<div class="tile abs" style="top:3405px;left:730px;width:450px;height:237px;background:linear-gradient(180deg,#a5c4df 0%,#4e6e8d 55%,#eceff1 100%)" role="img" aria-label="Blue house with white picket fence"></div>
<div class="tile abs" style="top:3661px;left:17px;width:226px;height:238px;background:linear-gradient(180deg,#3c5430 0%,#a5b39a 55%,#4a7233 100%)" role="img" aria-label="White ornamental fence along a hedge"></div>
<div class="tile abs" style="top:3661px;left:260px;width:453px;height:238px;background:linear-gradient(180deg,#6e8159 0%,#b68a5f 50%,#4f7b2f 100%)" role="img" aria-label="Cedar wood fence around a backyard"></div>
<div class="tile abs" style="top:3661px;left:730px;width:450px;height:238px;background:linear-gradient(135deg,#7d625e 0%,#5c7944 50%,#272a33 100%)" role="img" aria-label="Black iron fence with spear finials"></div>

<section class="reviews abs">
  <h2 class="heading reviews-title abs">What our clients say</h2>
  <svg class="arrow abs" style="left:1000px" viewBox="0 0 34 34"><path d="M23 17H11m5-6-6 6 6 6" stroke="#8b90a0" stroke-width="2" fill="none" stroke-linecap="round" stroke-linejoin="round"/></svg>
  <svg class="arrow abs" style="left:1051px" viewBox="0 0 34 34"><circle cx="17" cy="17" r="17" fill="#ffffff"/><path d="M11 17h12m-5-6 6 6-6 6" stroke="#e0262e" stroke-width="2" fill="none" stroke-linecap="round" stroke-linejoin="round"/></svg>
  <blockquote class="quote abs" style="left:116px">"Yardline Works exceeded our expectations from start to finish. The team was punctual, courteous, and the quality of our new wood fence is outstanding. We couldn't be happier with the results!"<cite>Dorian K.</cite></blockquote>
  <blockquote class="quote abs" style="left:616px">"Professional, reliable, and efficient. Yardline Works installed our automatic gate seamlessly and answered all our questions with patience. Highly recommend for anyone needing fencing or gate services."<cite>Wren L.</cite></blockquote>
</section>

<section class="cta abs" style="top:4376px">
  <h2 class="heading cta-title abs">Ready to transform<br>your property?</h2>
  <p class="cta-text abs">Lorem ipsum dolor sit amet, consectetur adipiscing elit, sed do eiusmod tempor incididunt ut labore et dolore magna aliqua. Ut enim ad minim veniam, quis nostrud exercitation.</p>
  <a class="btn cta-btn abs" href="#">Get a free quote</a>
</section>

<footer>
  <div class="footer-brand abs">Yardline Works</div>
  <a class="foot-link abs active" style="left:551px" href="#">Home</a>
  <a class="foot-link abs" style="left:617px" href="#">About us</a>
  <a class="foot-link abs" style="left:713px" href="#">Our services</a>
  <a class="foot-link abs" style="left:838px" href="#">Portfolio</a>
  <a class="foot-link abs" style="left:942px" href="#">FAQ</a>
  <a class="foot-link abs" style="left:994px" href="#">Contact us</a>
  <p class="copyright abs">Copyright 2025© Yardline Works. All right reserved.</p>
  <span class="social abs" style="left:868px"></span>
  <span class="social abs" style="left:914px"></span>
  <span class="social abs" style="left:960px"></span>
  <span class="social abs" style="left:1006px"></span>
  <span class="social abs" style="left:1052px"></span>
</footer>

</body>
</html>
```